Web Design for UK Based Technology Company*

Norvexa is a new entrant in the data marketplace.
It is offering two direct API services to help clients access:
- Company Data
- Location Data
We also offer data services and consulting to help companies to integrate our API services and the data derived from them into their businesses. Our aim is to offer both the technology and services to help businesses use and integrate data better. It is a modern business built to support a modern world.

Target Market(s)

Business Professionals and decision makers

Industry/Entity Type

It Service

Number of Pages Required

5+ page

Font styles to use
Sans Serif

Colors

Designer to choose colors to be used in the design.

Requirements
Must have
• The full suite of PSD designs taking into account the layouts and wireframes supplied with which it will be compared. Focus on the homepage first. It has to have a consistent theme/feel. It has to fit with the logo.
Nice to have
• Simple, clean, a few strong ideas.
Should not have
• Cartoons, overdesign, loud colours.

```html
<!DOCTYPE html>
<html lang="en">
<head>
<meta charset="utf-8">
<title>Norvexa – Richer Data to Drive Your Business</title>
<link href="https://fonts.googleapis.com/css2?family=Lato:wght@400;700&display=swap" rel="stylesheet">
<style>
:root{
  --navy:#13466d;
  --deep:#1b5e8c;
  --sky:#2b8fd6;
  --title:#2a8cd0;
  --ink:#1e1e1e;
  --grey:#ededed;
  --footer:#3a3a3a;
  --white:#ffffff;
}
*{box-sizing:border-box;margin:0;padding:0}
html,body{width:1200px;height:4796px;overflow:hidden}
body{position:relative;font-family:'Lato',sans-serif;color:var(--ink);background:var(--white)}
.abs{position:absolute}
svg.ic{width:18px;height:18px;vertical-align:-3px;margin-left:6px}
.btn{position:absolute;display:flex;align-items:center;justify-content:center;border-radius:28px;color:var(--white);font-size:18px;height:54px}
.btn.dark{background:var(--deep)}
.btn.light{background:var(--sky)}

/* header */
.brand{left:89px;top:38px;font-size:50px;font-weight:700;color:var(--navy);letter-spacing:1px;display:flex;align-items:center;gap:16px}
.brand i{display:block;width:34px;height:34px;border-radius:50%;background:var(--sky)}
.topbar{left:505px;top:28px;font-size:16px;color:var(--navy);display:flex;gap:14px;align-items:center}
.topbar svg{width:15px;height:15px;vertical-align:-2px;margin-right:5px;fill:var(--navy)}
.trial-top{left:942px;top:20px;width:166px;height:42px;font-size:17px;font-weight:700;background:var(--deep)}
.nav{left:505px;top:90px;display:flex;gap:38px;font-size:18px;color:var(--navy)}

/* hero */
.hero-photo{left:0;top:140px;width:1200px;height:660px;background:linear-gradient(135deg,#2b5f8a 0%,#4d86b0 40%,#86b0cf 60%,#2c5b86 100%)}
.hero-title{left:0;width:1200px;top:440px;text-align:center;color:var(--white);font-size:44px}
.hero-side{color:var(--white);font-size:27px;text-align:center;line-height:40px;width:340px}

/* welcome */
.welcome-title{left:0;width:1200px;top:875px;text-align:center;font-size:36px}
.welcome-title span{color:var(--title)}
.welcome-text{left:115px;width:970px;top:942px;text-align:center;font-size:15px;line-height:36px}
.rule{height:1px;background:#cfcfcf}

.grey{background:var(--grey)}
.photo{position:absolute}
.card{position:absolute;background:var(--white);box-shadow:0 2px 10px rgba(0,0,0,.12)}
.card h2{position:absolute;left:48px;font-size:36px;font-weight:400;color:var(--navy)}
.card p{position:absolute;left:48px;width:520px;font-size:15px;line-height:32px}

.cta-title{left:0;width:1200px;top:2572px;text-align:center;font-size:32px;color:var(--title)}
.cta-text{left:0;width:1200px;top:2636px;text-align:center;font-size:15px;line-height:36px}

.demand-title{left:586px;top:2930px;font-size:30px;line-height:49px;color:var(--title)}
.demand-text{left:588px;width:524px;top:3030px;font-size:16px;line-height:36px;text-align:justify}
.demand-text li{list-style:none;display:flex;gap:10px;align-items:flex-start}
.demand-text li svg{flex:none;width:20px;height:20px;margin-top:8px}

.where-title{left:87px;top:3696px;font-size:30px;color:var(--title)}
.address{left:89px;top:3750px;font-size:17px;line-height:36px}
.address svg{width:15px;height:15px;fill:var(--navy);vertical-align:-2px;margin-right:4px}

.footer{left:0;top:4380px;width:1200px;height:416px;background:var(--footer)}
.fcol{position:absolute;top:4452px;color:var(--white)}
.fcol h3{font-size:27px;font-weight:400;margin-bottom:22px}
.fcol li{list-style:none;font-size:15px;line-height:36px}
.fcol li svg{width:16px;height:16px;vertical-align:-3px;margin-right:8px}
.legal{left:89px;top:4754px;font-size:12px;color:var(--white)}
.legal-links{right:89px;top:4753px;font-size:14px;color:var(--white)}
</style>
</head>
<body>
<svg width="0" height="0" style="position:absolute">
  <symbol id="arr" viewBox="0 0 20 20"><circle cx="10" cy="10" r="10" fill="currentColor"/><path d="M5 10h8M9.5 6l4 4-4 4" stroke="#13466d" stroke-width="2.4" fill="none"/></symbol>
  <symbol id="arr-w" viewBox="0 0 20 20"><circle cx="10" cy="10" r="10" fill="#fff"/><path d="M5 10h8M9.5 6l4 4-4 4" stroke="#2b8fd6" stroke-width="2.4" fill="none"/></symbol>
  <symbol id="arr-o" viewBox="0 0 20 20"><circle cx="10" cy="10" r="8.5" fill="none" stroke="#fff" stroke-width="1.8"/><path d="M6 10h7M10 7l3 3-3 3" stroke="#fff" stroke-width="1.8" fill="none"/></symbol>
  <symbol id="arr-b" viewBox="0 0 20 20"><circle cx="10" cy="10" r="10" fill="#2b8fd6"/><path d="M5 10h8M9.5 6l4 4-4 4" stroke="#fff" stroke-width="2.4" fill="none"/></symbol>
</svg>

<!-- header -->
<div class="abs brand"><i></i>NORVEXA</div>
<div class="abs topbar">
  <span><svg viewBox="0 0 16 16"><rect x="1" y="3" width="14" height="10" rx="2"/></svg>CONTACT US</span><span>|</span>
  <span><svg viewBox="0 0 16 16"><path d="M3 1l3 3-2 2c1 2 3 4 5 5l2-2 3 3-2 3C6 15 1 10 1 3z"/></svg>0300 000 000</span><span>|</span>
  <span><svg viewBox="0 0 16 16"><circle cx="8" cy="5" r="4"/><path d="M1 16c0-5 14-5 14 0z"/></svg>LOGIN</span>
</div>
<div class="btn trial-top">Free Trial<svg class="ic" style="color:#fff"><use href="#arr"/></svg></div>
<div class="abs nav"><span>COMPANY DATA</span><span>LOCATION DATA</span><span>SERVICES</span><span>ABOUT US</span></div>

<!-- hero -->
<div class="abs hero-photo" role="img" aria-label="Photo of a man in glasses studying floating data screens"></div>
<svg class="abs" style="left:0;top:540px" width="1200" height="270" viewBox="0 0 1200 270">
  <path d="M0 30 Q300 95 560 140 L600 230 L0 250 Z" fill="#1b5e8c"/>
  <path d="M1200 15 Q900 90 640 140 L600 230 L1200 250 Z" fill="#2b8fd6"/>
  <path d="M0 250 L600 230 L1200 250 L1200 270 L0 270 Z" fill="#fff"/>
  <path d="M0 258 Q300 225 600 218 Q900 225 1200 258" stroke="#2b8fd6" stroke-width="4" fill="none"/>
  <path d="M0 242 Q300 215 600 205 Q900 215 1200 242" stroke="#fff" stroke-width="3" fill="none"/>
</svg>
<div class="abs hero-title">Richer Data to Drive Your Business</div>
<div class="btn dark" style="left:385px;top:537px;width:206px">Location API<svg class="ic" style="color:#fff"><use href="#arr"/></svg></div>
<div class="btn light" style="left:608px;top:537px;width:206px">Company API<svg class="ic"><use href="#arr-w"/></svg></div>
<div class="abs hero-side" style="left:70px;top:643px">Comprehensive Company Information</div>
<div class="abs hero-side" style="left:795px;top:643px">Bring Mapping Data Into Your Business</div>
<div class="abs" style="left:543px;top:636px;width:112px;height:112px;border-radius:50%;background:#fff"></div>

<!-- welcome -->
<div class="abs welcome-title">Welcome to <span>Norvexa</span></div>
<div class="abs welcome-text">
Norvexa is setup for connected world. A world where data is integrated, comprehensive and useful. Where systems are designed to cooperate to make businesses more efficient. For this purpose we have focused on two key areas of work - location and company data.<br>
Our Postcode API, is the most current in the marketplace, helping anyone pinpoint a map simply by providing a postcode. This allows you to assign a location to your postcode-level business data. We also provide an Address API, giving you an address for any postcode along with it's coordinate on the ground. We also supply base maps for customers looking to use maps on their websites. And we supply a wide range of bespoke GIS services, for more specific mapping work.<br>
For company data we have restructured Registry Hall data into something more useful and practical for businesses. Just supply one or more company numbers and we can send you back detailed company information covering a raft of data. Better still this data can be supplied either as a file or by API so you can receive it in the format you prefer.
</div>

<!-- products -->
<div class="abs grey" style="left:0;top:1334px;width:1200px;height:1168px"></div>
<div class="abs rule" style="left:108px;top:1334px;width:984px"></div>
<div class="photo" style="left:73px;top:1416px;width:520px;height:463px;background:linear-gradient(120deg,#2e2f35,#5b6470 55%,#c9d6e2)" role="img" aria-label="Photo of a hand pointing a pen at charts on a monitor"></div>
<div class="card" style="left:526px;top:1460px;width:601px;height:374px">
  <h2 style="top:88px">COMPANY API</h2>
  <p style="top:140px">You supply one or more company numbers - We send back everything via a simple API or CSV file</p>
  <div class="btn dark" style="left:49px;top:223px;width:202px">Find Out More<svg class="ic" style="color:#fff"><use href="#arr"/></svg></div>
  <div class="btn light" style="left:272px;top:223px;width:206px">Free Trial<svg class="ic"><use href="#arr-w"/></svg></div>
</div>
<div class="photo" style="left:606px;top:1959px;width:521px;height:463px;background:linear-gradient(135deg,#f4f7fa,#cfe0ef 50%,#7fb0d8)" role="img" aria-label="Photo of printed bar and pie charts"></div>
<div class="card" style="left:73px;top:2003px;width:600px;height:374px">
  <h2 style="top:88px">LOCATION API</h2>
  <p style="top:140px">You send us a postcode we send you the location. Or you send us the location, we send back the postcode: API or CSV.</p>
  <div class="btn dark" style="left:49px;top:223px;width:206px">Find Out More<svg class="ic" style="color:#fff"><use href="#arr"/></svg></div>
  <div class="btn light" style="left:273px;top:223px;width:206px">Free Trial<svg class="ic"><use href="#arr-w"/></svg></div>
</div>
<div class="abs rule" style="left:108px;top:2502px;width:984px"></div>

<!-- cta -->
<div class="abs cta-title">GO AHEAD: TEST OUR DATA; OR LET'S TALK IT THROUGH...</div>
<div class="abs cta-text">If you are confident you know what you want, why not start a trial? It's free of charge and you can test the service for a limited time,<br>If you are not so sure or you have a very specific requirements then talk to our consultants.</div>
<div class="btn dark" style="left:366px;top:2726px;width:225px">Call: 888 888 888<svg class="ic" style="color:#fff"><use href="#arr"/></svg></div>
<div class="btn light" style="left:608px;top:2726px;width:207px">Send an Email<svg class="ic"><use href="#arr-w"/></svg></div>

<!-- demanding -->
<div class="abs grey" style="left:0;top:2861px;width:327px;height:720px"></div>
<div class="photo" style="left:63px;top:3028px;width:462px;height:385px;background:radial-gradient(ellipse at 50% 60%,#5aa8ff,#134a9a 45%,#081a3c)" role="img" aria-label="Digital illustration of glowing data bars"></div>
<div class="abs demand-title">DEMANDING DATA REQUIREMENTS?<br>LOOK NO FURTHER</div>
<div class="abs demand-text">
<p>Most businesses looking for our help have complex data requirements they need to piece together. It may be they have an in-house team, but if not, we can help with:</p>
<ul>
<li><svg><use href="#arr-b"/></svg>Connecting our API into existing systems and software</li>
<li><svg><use href="#arr-b"/></svg>Helping with more complex business or location data supply</li>
<li><svg><use href="#arr-b"/></svg>Placing experienced staff on site to assist with mapping and data projects</li>
<li><svg><use href="#arr-b"/></svg>Helping businesses automate and digitally transform</li>
</ul>
<p>So if you want us to help you take your integrations up a notch, then let's talk. Please call 0000 000 000 or</p>
</div>
<div class="btn light" style="left:588px;top:3447px;width:242px;height:52px;font-size:16px">BESPOKE SERVICES<svg class="ic"><use href="#arr-w"/></svg></div>

<!-- where -->
<div class="abs grey" style="left:872px;top:3581px;width:328px;height:539px"></div>
<div class="abs" style="left:543px;top:3661px;width:594px;height:385px;background:linear-gradient(135deg,#eef0e6,#e3e6d8 60%,#c9dce8)" role="img" aria-label="Street map showing the office location"></div>
<div class="abs where-title">WHERE IS NORVEXA?</div>
<div class="abs address">
<svg viewBox="0 0 16 16"><path d="M8 0a6 6 0 0 0-6 6c0 5 6 10 6 10s6-5 6-10a6 6 0 0 0-6-6z"/></svg>Second Floor, 12 Meridian Yard<br>Halden Park<br>Thornbury Vale<br>Kestford KT4 2LP<br>
<svg viewBox="0 0 16 16"><path d="M3 1l3 3-2 2c1 2 3 4 5 5l2-2 3 3-2 3C6 15 1 10 1 3z"/></svg>Contact: 0000 000 000
</div>
<div class="btn light" style="left:89px;top:3945px;width:205px">Send an Email
<svg style="width:20px;height:14px;margin-left:10px" viewBox="0 0 20 14"><rect width="20" height="14" rx="1" fill="#fff"/><path d="M0 0l10 8 10-8" stroke="#2b8fd6" stroke-width="2" fill="none"/></svg></div>

<!-- lower band -->
<svg class="abs" style="left:0;top:4120px" width="1200" height="262" viewBox="0 0 1200 262">
  <path d="M0 10 Q300 40 600 50 Q900 40 1200 10 L1200 262 L0 262 Z" fill="#2b8fd6"/>
  <path d="M0 30 Q300 60 560 90 L600 200 L0 262 Z" fill="#13466d"/>
  <path d="M1200 30 Q900 60 640 90 L600 200 L1200 262 Z" fill="#1b5e8c"/>
  <path d="M0 0 L1200 0 L1200 10 Q900 40 600 50 Q300 40 0 10 Z" fill="#fff"/>
</svg>
<div class="abs" style="left:543px;top:4181px;width:112px;height:112px;border-radius:50%;background:#fff"></div>

<!-- footer -->
<div class="abs footer"></div>
<div class="fcol" style="left:89px"><h3>COMPANY DATA</h3><ul>
<li><svg><use href="#arr-o"/></svg>Company Information</li><li><svg><use href="#arr-o"/></svg>Alerts and Notifications</li><li><svg><use href="#arr-o"/></svg>Contact Information</li><li><svg><use href="#arr-o"/></svg>Financial information</li><li><svg><use href="#arr-o"/></svg>Other Data Services</li></ul></div>
<div class="fcol" style="left:396px"><h3>LOCATION DATA</h3><ul>
<li><svg><use href="#arr-o"/></svg>Postcode Lookup</li><li><svg><use href="#arr-o"/></svg>Address Lookup</li><li><svg><use href="#arr-o"/></svg>Base Mapping</li><li><svg><use href="#arr-o"/></svg>Boundaries</li><li><svg><use href="#arr-o"/></svg>Bespoke Mapping</li></ul></div>
<div class="fcol" style="left:712px"><h3>SERVICES</h3><ul>
<li><svg><use href="#arr-o"/></svg>API / Integrations</li><li><svg><use href="#arr-o"/></svg>Licensing / IPR</li><li><svg><use href="#arr-o"/></svg>Complex Location Data</li><li><svg><use href="#arr-o"/></svg>Digital Transformation</li></ul></div>
<div class="fcol" style="left:997px"><h3>NORVEXA</h3><ul>
<li><svg><use href="#arr-o"/></svg>Pricing</li><li><svg><use href="#arr-o"/></svg>About Us</li><li><svg><use href="#arr-o"/></svg>Contact Us</li><li><svg><use href="#arr-o"/></svg>Free Trial</li><li><svg><use href="#arr-o"/></svg>Login</li></ul></div>
<div class="abs rule" style="left:89px;top:4738px;width:1022px;background:#666"></div>
<div class="abs legal">Copyrights © 2019. All Rights Reserved.</div>
<div class="abs legal-links">Sitemap &nbsp;|&nbsp; Terms &amp; of Use &nbsp;|&nbsp; Privacy Policy &nbsp;|&nbsp; Contact us</div>
</body>
</html>
```